Bluegate Lending Template Design

We need a corporate letterhead template (word) and slide show template (PowerPoint) designed for our Motor Vehicle finance business.

Bluegate Lending provides motor vehicle finance to the credit impaired. Please feel free to visit our website www.bluegatelending.com

Both templates (word and PowerPoint) must include the Bluegate logo (attached to this project) and can be very similar in design.

We are after something creative yet professional in design.

Please feel free to ask any questions.

Thank you
Marlene

```html
<!DOCTYPE html>
<html lang="en">
<head>
<meta charset="utf-8">
<title>Bluegate Lending Letterhead</title>
<link rel="stylesheet" href="https://fonts.googleapis.com/css2?family=EB+Garamond:wght@400;600&display=swap">
<style>
  :root {
    --green: #1f9e3a;
    --green-bright: #2bb24a;
    --charcoal: #3d3d3d;
    --grey: #6b6b6b;
    --ink: #333333;
    --paper: #ffffff;
  }
  * { margin: 0; padding: 0; box-sizing: border-box; }
  html, body { width: 928px; height: 1200px; overflow: hidden; background: var(--paper); }
  .letterhead {
    position: relative;
    width: 928px;
    height: 1200px;
    background: var(--paper);
    font-family: "EB Garamond", Georgia, serif;
    color: var(--ink);
  }
  .brand {
    position: absolute;
    left: 58px;
    top: 58px;
    display: flex;
    align-items: center;
    gap: 22px;
  }
  .brand-mark {
    width: 96px;
    height: 96px;
    background: var(--grey);
  }
  .brand-name {
    font-family: "EB Garamond", Georgia, serif;
    font-weight: 600;
    font-size: 40px;
    letter-spacing: 0.5px;
    color: var(--green);
    white-space: nowrap;
  }
  .contact {
    position: absolute;
    right: 44px;
    top: 60px;
    list-style: none;
    text-align: right;
    font-size: 13.5px;
    line-height: 20.5px;
    color: var(--ink);
  }
  .contact li {
    display: flex;
    justify-content: flex-end;
    align-items: center;
    gap: 8px;
  }
  .contact svg { width: 11px; height: 11px; fill: var(--green); flex: none; }
  .footer {
    position: absolute;
    left: 0;
    bottom: 0;
    width: 928px;
    height: 110px;
  }
  .footer svg.bands { position: absolute; left: 0; top: 0; }
  .website {
    position: absolute;
    left: 726px;
    top: 27px;
    font-size: 15px;
    color: var(--paper);
    letter-spacing: 0.2px;
  }
  .web-icon {
    position: absolute;
    left: 682px;
    top: 24px;
    width: 28px;
    height: 28px;
  }
</style>
</head>
<body>
<main class="letterhead">
  <header>
    <div class="brand">
      <div class="brand-mark"></div>
      <div class="brand-name">Bluegate Lending</div>
    </div>
    <ul class="contact">
      <li>Po Box 418, Northcote VIC 3070
        <svg viewBox="0 0 12 12"><path d="M6 0.5a3.8 3.8 0 0 0-3.8 3.8C2.2 7.2 6 11.5 6 11.5s3.8-4.3 3.8-7.2A3.8 3.8 0 0 0 6 0.5zm0 5.2a1.4 1.4 0 1 1 0-2.8 1.4 1.4 0 0 1 0 2.8z"/></svg>
      </li>
      <li>1300 482 615
        <svg viewBox="0 0 12 12"><path d="M2.6 0.8l1.8 0.2 0.9 2.6-1.2 1a7 7 0 0 0 3.3 3.3l1-1.2 2.6 0.9 0.2 1.8c-0.2 1-1 1.6-2 1.6C5 11 1 7 1 2.8c0-1 0.6-1.8 1.6-2z"/></svg>
      </li>
      <li>03 9486 2173
        <svg viewBox="0 0 12 12"><path d="M3 1h5l1 1v2H3zM1.5 4.5h9a1 1 0 0 1 1 1V9h-2v2h-7V9h-2V5.5a1 1 0 0 1 1-1zM3.5 8v2h5V8z"/></svg>
      </li>
      <li>info@bluegatelending.com
        <svg viewBox="0 0 12 12"><path d="M1 2.5h10v7H1zm1 1v0.4l4 2.7 4-2.7V3.5zm0 1.6v3.4h8V5.1L6 7.8z"/></svg>
      </li>
    </ul>
  </header>

  <footer class="footer">
    <svg class="bands" width="928" height="110" viewBox="0 0 928 110">
      <rect x="0" y="23" width="660" height="16" fill="var(--charcoal)"/>
      <path d="M0 39H928V54H0z" fill="var(--green)"/>
      <path d="M628 39C650 39 652 0 690 0H928V54H628z" fill="var(--green)"/>
    </svg>
    <svg class="web-icon" viewBox="0 0 28 28">
      <circle cx="14" cy="14" r="14" fill="var(--green-bright)"/>
      <rect x="7.5" y="8.5" width="13" height="8.5" rx="1" fill="none" stroke="#ffffff" stroke-width="2"/>
      <rect x="5.5" y="18.5" width="17" height="2" fill="#ffffff"/>
    </svg>
    <span class="website">www.bluegatelending.com</span>
  </footer>
</main>
</body>
</html>
```